skyMARLOW Helicopter Tour WordPress Website Design

SkyMARLOW (skymarlow-tours.example) is a premium helicopter tour company offering scenic flights in two Florida cities: Tampa and Sarasota. We are seeking a full Wordpress website redesign that is modern, upbeat, inviting, and highly conversion‑focused. The new site should feel energetic and trustworthy, reflect the excitement of helicopter sightseeing, and maintain our recognizable SkyMARLOW color palette—while updating the overall look to feel fresh, clean, and current.
The website must be SEO‑friendly, mobile‑optimized, and easy to navigate. It should highlight our 5‑star customer reviews, showcase our tours clearly, and integrate seamlessly with TicketPine for instant online booking. The design should support a premium aviation experience while remaining friendly and accessible to tourists, families, couples, and adventure seekers.

These elements are essential and must be included in the design:

Brand & UX:
- Modern, upbeat, inviting design
- SEO‑friendly structure and layout
- Easy navigation and clear user flow
- Light grey “SM” background logo watermark (as used on current site)
- Clean, aviation‑inspired typography and layout

Conversion Features:
- Instant booking above the fold (TicketPine integration)
- Live Reviewly Reviews carousel
- Tour comparison table (duration, route, price, etc.)
- FAQ expandable section
- Gift Cards page (highlighted as a major offering)
- What to Expect timeline (Arrive → Check‑In → Safety Briefing → Flight → Photos)
- Weather transparency widget (clear messaging about weather‑dependent flights

Content Structure:
- Separate pages for Tampa, Sarasota, and Gender Reveal Flights
- Pilot/Team profiles with short bios
- Highlighted features:
- Doors‑Off option
- Sunset flights
- Romantic packages
- Champagne add‑ons

Colors:
Use the existing SkyMARLOW palette as the foundation, but modernize it.
- Background: Clean with the light grey “SM” watermark integrated tastefully.
The overall color direction should feel bright, premium, energetic, and trustworthy

Target Market(s)

Tourists visiting Tampa or Sarasota, Families looking for memorable activities, Couples seeking romantic experiences (sunset flights, proposals, anniversaries), Adventure seekers and content creators, Locals celebrating birthdays, holidays, or special occasions, Gender reveal clients looking for a unique aerial reveal experience

Industry/Entity Type

Travel & Tourism / Aviation / Helicopter Tours / Experience‑based Activities

Requirements
Must have
• These elements are essential and must be included in the design: Brand & UX - Modern, upbeat, inviting design / SEO‑friendly structure and layout / Easy navigation and clear user flow / Light grey “SM” background logo watermark (as used on current site) / Clean, aviation‑inspired typography and layout
Nice to have
• Interactive route map showing flight paths / Subtle motion or parallax effects in hero sections / Animated icons or micro‑interactions / Social media integration (Instagram grid, TikTok clips) / Sticky mobile booking bar / Video header or short aerial footage loop / Subtle aviation‑themed graphic elements (rotor blur, sky gradients, etc.
Should not have
• No dark, heavy, or overly moody themes / No outdated fonts or overly playful typography / No cluttered layouts or excessive text blocks / No stocky, generic tourism imagery / No slow‑loading animations or heavy effects that hurt SEO

```html
<!DOCTYPE html>
<html lang="en">
<head>
<meta charset="utf-8">
<title>skyMARLOW – Helicopter Tours over Tampa &amp; Sarasota</title>
<link rel="stylesheet" href="https://fonts.googleapis.com/css2?family=Audiowide&family=Nunito+Sans:wght@400;600;700;800&display=swap">
<style>
:root{
  --blue:#0b46c8;
  --blue-dark:#0836a3;
  --blue-soft:#e7eefb;
  --blue-pale:#cddcf7;
  --ink:#1c1c1f;
  --text:#3b3f48;
  --muted:#6b7180;
  --grey-panel:#f2f3f5;
  --dark:#1a1b1e;
  --footer:#121214;
  --white:#ffffff;
  --gold:#f5b400;
  --watermark:#eceef1;
}
*{box-sizing:border-box;margin:0;padding:0}
html,body{width:1200px;height:4713px;overflow:hidden}
body{position:relative;background:var(--white);font-family:"Nunito Sans",Arial,sans-serif;color:var(--text);font-size:12px}
.abs{position:absolute}
.display{font-family:"Audiowide","Arial Black",sans-serif;color:var(--ink);text-transform:uppercase;font-weight:400}
.btn{display:inline-flex;align-items:center;gap:8px;background:var(--blue);color:var(--white);font-weight:700;font-size:12px;text-transform:uppercase;border-radius:4px;padding:0 16px;height:38px;letter-spacing:.2px}
.btn svg{width:22px;height:14px}
.btn-outline{background:var(--white);color:var(--blue);border:1.5px solid var(--blue)}
.dots{display:flex;gap:8px;justify-content:center}
.dots i{width:8px;height:8px;border-radius:50%;background:#d5d8de;display:block}
.dots i.on{background:var(--blue)}
.watermark{position:absolute;font-family:"Nunito Sans",Arial,sans-serif;font-weight:800;color:var(--watermark);letter-spacing:-10px;line-height:1;z-index:0;pointer-events:none}

/* header */
.site-header{top:0;left:0;width:1200px;height:80px;background:var(--white);z-index:5}
.brand{display:flex;align-items:center;gap:6px;font-weight:800;color:var(--blue);font-size:17px}
.brand .mark{width:14px;height:14px;border-radius:50%;background:var(--blue)}
.main-nav{top:42px;left:278px;display:flex;gap:15px;font-size:11px;font-weight:700;color:var(--ink)}
.main-nav a{color:inherit;text-decoration:none}
.main-nav a.active{color:var(--blue)}
.weather{top:34px;left:882px;font-size:10px;color:var(--ink);text-align:right;line-height:1.2}
.weather b{font-size:11px}

/* hero */
.hero{top:80px;left:123px;width:954px;height:470px;border-radius:8px;overflow:hidden;background:linear-gradient(180deg,#c7d8fb 0%,#e3ebfc 55%,#f4f7fe 100%)}
.hero-title{top:63px;width:954px;text-align:center;font-size:32px;letter-spacing:1px}
.hero-sub{top:108px;width:954px;text-align:center;font-size:14px;color:var(--text)}
.hero-ctas{top:152px;width:954px;display:flex;justify-content:center;gap:10px}
.hero-trust{top:218px;width:954px;text-align:center;font-size:14px;color:var(--ink);font-weight:600}
.hero-loc{top:255px;width:954px;text-align:center;font-size:10px;color:var(--text)}
.loc-toggle{top:284px;width:954px;display:flex;justify-content:center;gap:8px}
.loc-toggle span{width:84px;height:28px;border-radius:14px;border:1.5px solid var(--blue);font-size:11px;display:flex;align-items:center;justify-content:center;background:var(--white);color:var(--ink)}
.loc-toggle span.on{background:var(--blue);color:var(--white)}
.search-box{top:424px;left:221px;width:756px;height:110px;background:var(--white);border-radius:8px;box-shadow:0 4px 18px rgba(20,40,90,.12);padding:14px 20px;z-index:3}
.trip-type{display:flex;gap:14px;font-size:10px;color:var(--muted)}
.trip-type span::before{content:"";display:inline-block;width:6px;height:6px;border-radius:50%;border:1px solid #999;margin-right:4px}
.trip-type span.on{color:var(--blue)}
.trip-type span.on::before{background:var(--blue);border-color:var(--blue)}
.search-fields{display:flex;gap:8px;margin-top:16px;align-items:flex-end}
.field label{display:block;font-size:10px;font-weight:700;color:var(--ink);margin-bottom:5px}
.field div{height:26px;background:#f0f1f3;border-radius:3px;font-size:8px;color:#999;padding:0 8px;display:flex;align-items:center;justify-content:space-between}
.pax{display:flex;align-items:center;gap:6px}
.pax i{width:12px;height:12px;border-radius:50%;background:#333;display:block}
.btn-search{height:30px;width:96px;justify-content:center;font-size:10px;margin-left:6px}

/* choose */
.choose-title{top:590px;width:1200px;text-align:center;font-size:32px}
.tour-slide{top:651px;left:123px;width:954px;height:362px;border-radius:8px;overflow:hidden;background:linear-gradient(100deg,#6e8b7c 0%,#a7b6a4 35%,#d5c7ae 60%,#8fa5b6 100%)}
.tour-card{top:18px;left:31px;width:390px;height:328px;background:rgba(40,40,42,.9);border-radius:8px;padding:36px 28px;color:#e8e8ea}
.tour-card h3{font-size:18px;font-weight:600;color:var(--white);margin-bottom:14px}
.tour-card p{font-size:11px;line-height:1.62;margin-bottom:14px}
.tour-card ul{list-style:none;font-size:11px;line-height:1.9}
.tour-card li::before{content:"";display:inline-block;width:7px;height:7px;border-radius:50%;background:var(--white);margin-right:8px}
.tour-card .btn{margin-top:20px;background:transparent;border:1px solid var(--white);height:38px;font-weight:600}

/* elevate */
.elevate-title{top:1120px;left:123px;font-size:32px;line-height:1.4}
.elevate-text{top:1138px;left:673px;width:330px;font-size:10.5px;line-height:1.9;color:var(--text)}
.experience-cards{top:1297px;left:123px;display:flex;gap:13px}
.xp-card{width:224px;height:276px;background:var(--blue-soft);border-radius:6px;padding:8px 8px 0}
.xp-card .photo{height:128px;border-radius:3px}
.xp-card h4{font-size:17px;color:var(--ink);font-weight:600;margin:14px 6px 6px}
.xp-card p{font-size:10.5px;line-height:1.5;margin:0 6px;color:var(--text)}
.xp-card a{display:block;margin:14px 6px 0;font-size:11px;font-weight:700;color:var(--blue);text-decoration:none}

/* trust */
.trust{top:1637px;left:123px;width:954px;height:474px;border-radius:8px;background:linear-gradient(180deg,#2a2b2f,#1b1c1f 60%,#232427);overflow:hidden;color:#d4d6dc}
.trust h2{top:52px;width:954px;text-align:center;font-size:32px;line-height:1.3;color:var(--white)}
.trust p{top:148px;width:954px;text-align:center;font-size:10.5px;line-height:1.9}
.badges{top:211px;left:43px;display:flex;gap:42px}
.badge{width:184px;height:184px;border-radius:50%;background:var(--white);border:6px solid #c9cbd1;border-bottom-color:var(--blue);position:relative;display:flex;flex-direction:column;align-items:center;justify-content:center;gap:10px}
.badge::after{content:"";position:absolute;bottom:-10px;left:50%;margin-left:-7px;width:14px;height:14px;border-radius:50%;background:var(--blue)}
.badge svg{width:54px;height:54px}
.badge span{font-size:13.5px;font-weight:700;color:var(--ink)}

/* gift */
.gift-title{top:2168px;width:1200px;text-align:center;font-size:32px;line-height:1.4}
.gift-sub{top:2258px;width:1200px;text-align:center;font-size:10.5px}
.gift-row{top:2301px;left:123px;width:954px;height:201px;overflow:hidden;display:flex;gap:14px}
.gift-card{flex:0 0 330px;height:201px;position:relative;border-radius:2px}
.gift-card .btn{position:absolute;height:22px;font-size:8px;padding:0 10px;background:transparent;border:1px solid var(--white)}

/* pilots */
.pilots-panel{top:2643px;left:123px;width:470px;height:338px;background:var(--grey-panel);padding:52px 50px}
.pilots-panel h2{font-size:32px;margin-bottom:22px}
.pilots-panel p{font-size:10.5px;line-height:1.95}
.pilots-panel .btn{margin-top:28px}
.pilot-photo{top:2605px;left:576px;width:503px;height:416px;background:linear-gradient(160deg,#d9d7d2 0%,#c5b7a6 45%,#6b5b50 100%)}

/* reviews */
.reviews-title{top:3080px;width:1200px;text-align:center;font-size:32px;line-height:1.4}
.reviews-brand{top:3172px;width:1200px;text-align:center;font-size:34px;font-weight:700;color:var(--blue)}
.reviews-score{top:3222px;width:1200px;text-align:center;font-size:12px;font-weight:800;color:var(--ink)}
.reviews-score small{font-weight:400;font-size:10px;color:var(--text)}
.stars{color:var(--gold);letter-spacing:1px}
.review-row{top:3265px;left:0;width:1200px;height:232px;overflow:hidden}
.review{position:absolute;top:0;width:317px;height:230px;background:var(--blue-soft);border-radius:4px;padding:26px 28px;text-align:center}
.review .q{position:absolute;top:10px;left:14px;font-size:46px;color:#c6d3ef;font-weight:800;line-height:1}
.review .g{position:absolute;top:14px;right:14px;width:14px;height:14px;border-radius:50%;border:2px solid #8aa6e0}
.review .av{width:40px;height:40px;border-radius:50%;margin:0 auto 8px;display:flex;align-items:center;justify-content:center;color:var(--white);font-weight:700;font-size:20px}
.review h5{font-size:13px;color:var(--ink)}
.review .when{font-size:10px;color:var(--muted)}
.review p{font-size:10.5px;line-height:1.9;margin-top:8px}

/* faq */
.faq{top:3603px;left:123px;width:954px;height:443px;background:var(--grey-panel)}
.faq-photo{top:17px;left:18px;width:373px;height:409px;border-radius:4px;background:linear-gradient(180deg,#3d5a7a 0%,#8a7e73 45%,#2b5d73 70%,#1f4d5e 100%)}
.faq h2{top:40px;left:419px;font-size:32px;line-height:1.4}
.faq-list{top:142px;left:419px;width:505px}
.faq-item{background:var(--white);border:1px solid #dcdfe4;border-radius:4px;height:40px;padding:0 22px;display:flex;align-items:center;justify-content:space-between;font-size:10.5px;color:var(--ink);margin-bottom:14px}
.faq-item i{width:17px;height:17px;border-radius:50%;background:#8a8e96;color:var(--white);font-style:normal;font-size:13px;display:flex;align-items:center;justify-content:center}
.faq-item.open{background:var(--blue-pale);border-color:#b7c9ee;height:auto;padding:18px 22px;display:block;position:relative}
.faq-item.open i{position:absolute;right:12px;top:14px;background:var(--blue)}
.faq-item.open p{font-size:10px;line-height:1.7;color:var(--text);margin-top:10px}
.faq .btn{top:380px;left:419px;position:absolute}

/* cta + footer */
.site-footer{top:4236px;left:0;width:1200px;height:477px;background:var(--footer);color:#c7c9cf}
.cta{top:4104px;left:123px;width:954px;height:253px;background:linear-gradient(90deg,#0b46c8,#0a3fb8);border-radius:6px;z-index:2;overflow:hidden;color:var(--white)}
.cta h2{top:66px;left:61px;font-size:32px;color:var(--white)}
.cta p{top:116px;left:61px;width:560px;font-size:13.5px;line-height:1.65;color:#dce5fb}
.cta .btn{top:170px;left:61px;position:absolute;background:transparent;border:1.5px solid var(--white)}
.cta-mark{top:70px;left:660px;font-size:150px;font-weight:800;color:var(--white);line-height:1;letter-spacing:-4px}
.foot-brand{top:190px;left:123px}
.foot-brand .brand{color:var(--white)}
.foot-about{top:250px;left:123px;width:300px;font-size:10.5px;line-height:1.8}
.socials{top:320px;left:123px;display:flex;gap:8px}
.socials i{width:22px;height:22px;border-radius:50%;border:1px solid #c7c9cf;display:block}
.foot-divider{top:180px;width:1px;height:190px;background:#3a3c42}
.foot-col{top:186px;font-size:10.5px;line-height:1.85}
.foot-col h6{font-size:13px;font-weight:600;color:var(--white);margin-bottom:8px;text-decoration:underline;text-underline-offset:4px}
.contact-line{display:flex;align-items:center;gap:8px;margin-bottom:12px}
.contact-line b{width:20px;height:20px;border-radius:50%;border:1px solid #c7c9cf;display:flex;align-items:center;justify-content:center}
.contact-line svg{width:10px;height:10px}
.copyright{top:446px;width:1200px;text-align:center;font-size:10px;color:#a4a7ae}
</style>
</head>
<body>

<svg width="0" height="0" style="position:absolute">
  <defs>
    <symbol id="heli" viewBox="0 0 22 14"><rect x="1" y="1" width="20" height="1.6" rx=".8" fill="currentColor"/><rect x="10" y="2" width="1.4" height="3" fill="currentColor"/><ellipse cx="9" cy="8" rx="5" ry="3.4" fill="currentColor"/><rect x="13" y="7" width="8" height="1.6" fill="currentColor"/><rect x="4" y="12" width="10" height="1.2" fill="currentColor"/></symbol>
  </defs>
</svg>

<div class="watermark" style="top:940px;left:470px;font-size:560px">SM</div>
<div class="watermark" style="top:2080px;left:700px;font-size:380px">SM</div>
<div class="watermark" style="top:2960px;left:-20px;font-size:280px">SM</div>

<header class="site-header abs">
  <div class="abs" style="top:26px;left:123px"><div class="brand"><span class="mark"></span>skyMARLOW</div></div>
  <nav class="main-nav abs">
    <a class="active" href="#">HOME</a><a href="#">TOURS ▾</a><a href="#">GIFT CARDS</a><a href="#">WHAT TO EXPECT</a><a href="#">REVIEWS</a><a href="#">OUR PILOTS</a><a href="#">FAQ</a><a href="#">CONTACT</a>
  </nav>
  <div class="weather abs"><b>21°</b> <svg width="16" height="10" viewBox="0 0 16 10"><path d="M4 9h9a3 3 0 0 0 0-6 4 4 0 0 0-7.5 1A2.5 2.5 0 0 0 4 9z" fill="#0b46c8"/></svg><br>Mostly cloudy</div>
  <a class="btn abs" style="top:35px;left:966px;height:31px;font-size:10px;padding:0 12px"><svg><use href="#heli"/></svg>BOOK NOW</a>
</header>

<section class="hero abs" role="img" aria-label="Pale blue sky with airliner and city skyline along the bottom">
  <h1 class="display hero-title abs">See Florida From a Whole New Altitude</h1>
  <p class="hero-sub abs">Premium helicopter tours over Tampa &amp; Sarasota — unforgettable views, 5-star experiences, instant booking.</p>
  <div class="hero-ctas abs">
    <a class="btn"><svg><use href="#heli"/></svg>Book Your Flight Now</a>
    <a class="btn btn-outline"><svg><use href="#heli"/></svg>View Tour Options</a>
  </div>
  <p class="hero-trust abs">FAA-certified pilots · Modern aircraft · Safety-first</p>
  <p class="hero-loc abs">Select Your Location</p>
  <div class="loc-toggle abs"><span>Tampa</span><span class="on">Sarasota</span></div>
</section>

<form class="search-box abs">
  <div class="trip-type"><span class="on">All</span><span>One Way</span><span>Round Trip</span></div>
  <div class="search-fields">
    <div class="field" style="width:142px"><label>FROM</label><div><span></span>⌖</div></div>
    <div class="field" style="width:142px"><label>TO</label><div><span></span>⌖</div></div>
    <div class="field" style="width:142px"><label>DATE</label><div>dd-mm-yyyy<span>▪</span></div></div>
    <div class="field"><label>PAX</label><div class="pax" style="background:none;padding:0"><i></i><span style="width:118px;height:26px;background:#f0f1f3;border-radius:3px;display:flex;align-items:center;justify-content:center">1</span><i></i></div></div>
    <span class="btn btn-search">SEARCH</span>
  </div>
</form>

<h2 class="display choose-title abs">Choose Your SkyMarlow</h2>
<section class="tour-slide abs" role="img" aria-label="Couple sharing a surprised, joyful moment outdoors after a proposal">
  <div class="tour-card abs">
    <h3>Romantic Helicopter Experience</h3>
    <p>A private helicopter flight crafted for life's most meaningful moments. Celebrate proposals, anniversaries, or once-in-a-lifetime surprises as you soar above Florida's stunning coastline—complete with breathtaking views, intimate privacy, and memories that last forever.</p>
    <ul><li><b>Duration:</b> 30 Minutes</li><li><b>Starting at:</b> <span style="color:#e23a3a">$399</span> <span style="font-size:7px">per couple</span></li><li><b>Badge:</b> Romantic</li></ul>
    <a class="btn"><svg><use href="#heli"/></svg>View Details</a>
  </div>
</section>
<div class="dots abs" style="top:1044px;width:1200px"><i></i><i></i><i class="on"></i><i></i></div>

<h2 class="display elevate-title abs">Elevate Your<br>Flight Experience</h2>
<p class="elevate-text abs">Not all helicopter tours are the same. SkyMARLOW's featured experiences let guests customize their flight to match their sense of adventure, celebration, or romance—turning a scenic tour into something truly unforgettable.</p>
<a class="btn abs" style="top:1227px;left:123px"><svg><use href="#heli"/></svg>Explore Experiences</a>

<div class="experience-cards abs">
  <article class="xp-card"><div class="photo" role="img" aria-label="View down from an open helicopter door over a city at dusk" style="background:linear-gradient(160deg,#3a4660,#8a6d4c 60%,#2e3a52)"></div><h4>Doors-Off Flights</h4><p>Feel the rush of open-air flying with unobstructed views—perfect for thrill-seekers and photographers.</p><a>LEARN MORE ›</a></article>
  <article class="xp-card"><div class="photo" role="img" aria-label="Passengers inside a helicopter cockpit during a golden hour flight" style="background:linear-gradient(160deg,#9fb9cf,#5f7686 55%,#c9b08a)"></div><h4>Sunset Flights</h4><p>Soar through golden hour as Florida's coastline glows below for a truly magical experience.</p><a>LEARN MORE ›</a></article>
  <article class="xp-card"><div class="photo" role="img" aria-label="Couple with headsets smiling inside a helicopter cabin" style="background:linear-gradient(160deg,#7d6a5e,#b8c4cc 55%,#e2e6ea)"></div><h4>Romantic Packages</h4><p>Private helicopter flights designed for proposals, anniversaries, and unforgettable moments together.</p><a>LEARN MORE ›</a></article>
  <article class="xp-card"><div class="photo" role="img" aria-label="Friends toasting with champagne beside a helicopter" style="background:linear-gradient(160deg,#bccbd6,#6f6a66 50%,#e4dcd2)"></div><h4>Champagne Add-Ons</h4><p>Celebrate your flight in style with champagne and premium touches before or after takeoff.</p><a>LEARN MORE ›</a></article>
</div>

<section class="trust abs">
  <h2 class="display abs">More Than a Flight — It's an<br>Experience You Can Trust</h2>
  <p class="abs">When you choose SkyMARLOW, you're choosing safety, professionalism, and an unforgettable way to see Florida from the sky.<br>Every detail of our tours is designed to deliver excitement without compromise—and memories that last long after landing.</p>
  <div class="badges abs">
    <div class="badge"><svg viewBox="0 0 54 54" fill="none" stroke="#0b46c8" stroke-width="2"><path d="M14 14h26l-3 8H17z"/><path d="M16 40c0-7 5-12 11-12s11 5 11 12v6H16z"/><path d="M27 30v14"/></svg><span>FAA-Certified Pilots</span></div>
    <div class="badge"><svg viewBox="0 0 54 54" fill="none" stroke="#0b46c8" stroke-width="2"><path d="M27 6c2 0 3 2 3 5v10l16 9v4l-16-4v10l5 4v3l-8-2-8 2v-3l5-4V30L8 34v-4l16-9V11c0-3 1-5 3-5z"/></svg><span>Modern Aircraft</span></div>
    <div class="badge"><svg viewBox="0 0 54 54" fill="none" stroke="#0b46c8" stroke-width="2"><path d="M16 30h6v16h-6zM22 32l6-10c2-3 5-2 5 1l-1 6h9c2 0 3 2 3 4l-3 10c-1 2-2 3-4 3H22"/><path d="M27 6l2 4 4 .5-3 3 1 4-4-2-4 2 1-4-3-3 4-.5z"/></svg><span>Top-Rated Flights</span></div>
    <div class="badge"><svg viewBox="0 0 54 54" fill="none" stroke="#0b46c8" stroke-width="2"><path d="M4 46l16-24 8 12 6-8 16 20z"/><circle cx="16" cy="12" r="4"/></svg><span>Breathtaking Views</span></div>
  </div>
</section>

<h2 class="display gift-title abs">Give an Experience<br>They'll Never Forget</h2>
<p class="gift-sub abs">Give more than a gift—give a once-in-a-lifetime experience soaring above Florida.</p>
<div class="gift-row abs">
  <div class="gift-card" role="img" aria-label="Navy blue birthday gift card with ribbon bow and script greeting" style="background:linear-gradient(90deg,#1d5fae,#0f2f6a 40%,#0c2b5f)"><span class="btn" style="left:168px;top:128px"><svg><use href="#heli"/></svg>BUY GIFT CARDS</span></div>
  <div class="gift-card" role="img" aria-label="Red anniversary gift card with hearts and script greeting" style="background:linear-gradient(180deg,#b8121c,#8a0b12)"><span class="btn" style="left:108px;top:84px"><svg><use href="#heli"/></svg>BUY GIFT CARDS</span></div>
  <div class="gift-card" role="img" aria-label="Pastel pink and blue gender reveal gift card with script lettering" style="background:linear-gradient(90deg,#c9d7f1,#f3dde6 45%,#fbe8ee)"><span class="btn" style="left:200px;top:120px;color:#0b46c8;border-color:#0b46c8;background:#fff"><svg><use href="#heli"/></svg>BUY GIFT CARDS</span></div>
</div>
<div class="dots abs" style="top:2533px;width:1200px"><i></i><i></i><i class="on"></i><i></i></div>

<section class="pilots-panel abs">
  <h2 class="display">Meet Our Pilots</h2>
  <p>When you fly with SkyMARLOW, you're in expert hands. Our pilots are FAA-certified professionals with thousands of flight hours and deep knowledge of Florida's coastline, skylines, and skies.<br>Each pilot is trained to the highest aviation standards and committed to delivering a safe, smooth, and unforgettable experience—whether it's your first helicopter flight or a once-in-a-lifetime moment.</p>
  <p style="margin-top:12px;font-weight:700;color:var(--ink)">Your safety is our mission.</p>
  <a class="btn"><svg><use href="#heli"/></svg>Meet Our Team</a>
</section>
<div class="pilot-photo abs" role="img" aria-label="Pilot in sunglasses standing confidently against a pale sky"></div>

<h2 class="display reviews-title abs">What Customers<br>Are Saying</h2>
<div class="reviews-brand abs">Reviewly</div>
<div class="reviews-score abs">EXCELLENT <span class="stars">★★★★★</span> <small>Based on <b>225</b> reviews</small></div>
<div class="review-row abs">
  <div class="review" style="left:-220px"><span class="g"></span><p style="margin-top:60px;text-align:right">Great flight, kind crew and lovely views over the bay all the way.</p></div>
  <div class="review" style="left:112px"><span class="q">“</span><span class="g"></span><div class="av" style="background:#3a2a22">M</div><h5>Marco Ellis</h5><div class="when">2 weeks ago</div><div class="stars">★★★★★</div><p>This was an Early Christmas gift for my 9yr old special needs son. Everything exceeded my expectations and Tomas our pilot did an amazing job . He was super friendly ...</p></div>
  <div class="review" style="left:443px"><span class="q">“</span><span class="g"></span><div class="av" style="background:#139a74">N</div><h5>Nadia Fuentes</h5><div class="when">2 weeks ago</div><div class="stars">★★★★★</div><p>Such a great experience! My husband booked us the romantic flight as a suprise it was absolutely adorable. Definitely need to have a good tour guide and I liked ours.</p></div>
  <div class="review" style="left:773px"><span class="q">“</span><span class="g"></span><div class="av" style="background:#c98a4a">R</div><h5>Rosa BELMONT</h5><div class="when">2 weeks ago</div><div class="stars">★★★★★</div><p>We had an incredible experience with SkyMarlow! From the moment we arrived, everything felt smooth, professional, and well organized. Our...</p></div>
  <div class="review" style="left:1104px"><span class="q">“</span><p style="margin-top:60px;text-align:left">We had a wonderful time, everything went smoothly</p></div>
</div>
<div class="dots abs" style="top:3530px;width:1200px"><i></i><i></i><i class="on"></i><i></i></div>

<section class="faq abs">
  <div class="faq-photo abs" role="img" aria-label="Aerial view of a waterfront city skyline at dusk"></div>
  <h2 class="display abs">Frequently<br>Asked Questions</h2>
  <div class="faq-list abs">
    <div class="faq-item">Is flying in a helicopter safe?<i>+</i></div>
    <div class="faq-item open">Are your pilots licensed and experienced?<i>−</i><p>Absolutely. Our pilots are FAA-certified professionals with extensive flight hours and local flight experience over Tampa and Sarasota airspace.</p></div>
    <div class="faq-item">Do you provide a safety briefing before the flight?<i>+</i></div>
  </div>
  <a class="btn"><svg><use href="#heli"/></svg>View All</a>
</section>

<footer class="site-footer abs">
  <div class="foot-brand abs"><div class="brand"><span class="mark" style="background:#fff"></span>skyMARLOW</div></div>
  <p class="foot-about abs">SkyMARLOW offers unforgettable helicopter tours over Tampa and Sarasota, delivering breathtaking views, professional pilots, and a premium aviation experience.</p>
  <div class="socials abs"><i></i><i></i><i></i></div>
  <div class="foot-divider abs" style="left:443px"></div>
  <div class="foot-divider abs" style="left:835px"></div>
  <div class="foot-col abs" style="left:494px"><h6>Main Links</h6>Home<br>Tours<br>Gift Cards<br>What to<br>Expect<br>Reviews<br>Our Pilots<br>FAQ<br>Contact</div>
  <div class="foot-col abs" style="left:670px"><h6>Resources</h6>FAQs<br>Terms of use<br>Terms of Service<br>Privacy Policy</div>
  <div class="foot-col abs" style="left:858px"><h6>Contact Us</h6>
    <div class="contact-line"><b><svg viewBox="0 0 10 10"><rect x="1" y="2" width="8" height="6" fill="none" stroke="#fff"/><path d="M1 2l4 3 4-3" fill="none" stroke="#fff"/></svg></b><span style="color:#4b80f0">info@skymarlow-tours.example</span></div>
    <div class="contact-line"><b><svg viewBox="0 0 10 10"><path d="M2 1l2 2-1 1.5a6 6 0 0 0 2.5 2.5L7 6l2 2-1 1.5C4 9 1 6 .5 2z" fill="#fff"/></svg></b>(555) 010-4477 | (555) 010-8368</div>
    <div class="contact-line"><b><svg viewBox="0 0 10 10"><path d="M5 9.5S1.5 6 1.5 4a3.5 3.5 0 0 1 7 0C8.5 6 5 9.5 5 9.5z" fill="#fff"/><circle cx="5" cy="4" r="1.2" fill="#121214"/></svg></b>Florida cities: Tampa and Sarasota</div>
  </div>
  <p class="copyright abs">Copyright © 2026 skyMARLOW. All Rights Reserved</p>
</footer>

<section class="cta abs">
  <h2 class="display abs">Ready For Takeoff?</h2>
  <p class="abs">See Tampa and Sarasota from a perspective few ever experience. Whether it's your first flight or a once-in-a-lifetime moment, your adventure starts here.</p>
  <a class="btn"><svg><use href="#heli"/></svg>Book Your Flight Now</a>
  <div class="cta-mark abs">SM</div>
</section>

</body>
</html>
```